UK Online Auction Site needs a clever design

We need a contemporary landing page and registration page design for a UK auction website, that look equally at home on PC's and tablets . The design should be fresh, bright, clean, professional, robust, and familiar. We would like to see something clever but functional.

Industry/Entity Type

Online

```html
<!DOCTYPE html>
<html lang="en">
<head>
<meta charset="utf-8">
<title>Bidwell – Shop By Categories</title>
<link rel="stylesheet" href="https://fonts.googleapis.com/css2?family=Open+Sans:wght@400;600&display=swap">
<style>
:root{
  --brand:#0a7bc8;
  --brand-dark:#0868a8;
  --ink:#333;
  --muted:#666;
  --line:#ddd;
  --topbar:#f3f3f3;
  --footer:#f0f0f0;
  --btn-grey:#555;
  --search-field:#fff;
}
*{box-sizing:border-box;margin:0;padding:0}
html,body{width:1200px;height:1015px;overflow:hidden;background:#fff;font-family:"Open Sans",sans-serif;color:var(--ink)}
.page{position:relative;width:1200px;height:1015px}
a{color:var(--brand);text-decoration:none}

.topbar{position:absolute;left:0;top:0;width:1200px;height:35px;background:var(--topbar);font-size:12px;line-height:35px;text-align:right;padding-right:74px}

.nav{position:absolute;right:74px;top:48px;display:flex;gap:15px;font-size:12px;letter-spacing:.5px}
.nav-item{display:flex;align-items:center;gap:5px;color:var(--ink)}
.nav-item svg{width:14px;height:14px;fill:#333}

.logo{position:absolute;left:74px;top:67px;width:166px;height:65px;display:flex;align-items:center;gap:8px;color:var(--brand);font-size:34px;font-weight:600}
.logo-mark{width:14px;height:14px;background:var(--brand);border-radius:50%}

.search{position:absolute;left:344px;top:78px;width:782px;height:54px;background:var(--brand);display:flex;align-items:center;padding:0 8px 0 20px}
.search-label{color:#fff;font-size:13px;letter-spacing:.5px;width:94px}
.search-box{flex:1;height:40px;background:var(--search-field);display:flex;align-items:center;border-radius:2px}
.search-cat{width:113px;height:100%;border-right:1px solid #ddd;font-size:12px;display:flex;align-items:center;padding-left:11px;gap:10px}
.search-cat::after{content:"";border:4px solid transparent;border-top-color:#333;margin-top:4px}
.search-input{flex:1}
.search-gear{width:14px;height:14px;border-radius:50%;border:3px solid #ccc;margin-right:25px}
.search-go{width:42px;height:30px;background:#444;margin-right:4px;border-radius:2px;display:flex;align-items:center;justify-content:center}
.search-go svg{width:18px;height:18px}

.rule{position:absolute;left:74px;width:1052px;height:1px;background:var(--line)}
.section-title{position:absolute;left:74px;top:162px;font-size:22px;font-weight:400;color:#444}

.tile{position:absolute;width:243px;overflow:hidden}
.tile-label{position:absolute;background:var(--brand);color:#fff;font-size:16px;line-height:19px;padding:9px 12px 8px 18px}
.ph{position:absolute;inset:0}

.box{position:absolute;top:655px;width:243px;height:232px;border:2px solid #e2e2e2;padding:18px 17px}
.box h2{font-size:18px;font-weight:400;color:#333;margin-bottom:11px}
.box p{font-size:12.5px;line-height:19.5px;color:var(--muted)}
.learn{position:absolute;left:17px;top:162px;font-size:11.5px;font-weight:600;letter-spacing:.5px}
.btns{display:flex;gap:5px;margin-top:20px}
.btn{color:#fff;font-size:11.5px;letter-spacing:1px;padding:7px 14px;border-radius:2px}
.btn-primary{background:var(--brand)}
.btn-secondary{background:var(--btn-grey)}
.box p.note{font-size:12px;margin-top:15px}

.confidence{padding:18px 6px 12px 11px}
.confidence h2{margin-bottom:8px}
.feature{display:flex;gap:9px;margin-bottom:7px}
.feature svg{width:30px;height:30px;flex:none;margin-top:2px}
.feature strong{display:block;font-weight:400;color:var(--brand);font-size:12.5px;line-height:15px}
.feature span{font-size:11px;line-height:14.5px;color:var(--muted);display:block}

.promo{position:absolute;left:884px;top:655px;width:243px;height:232px;border:2px solid #e2e2e2;background:linear-gradient(160deg,#262626 0%,#1c1c1c 70%,#5a6a80 100%)}

.footer{position:absolute;left:0;top:913px;width:1200px;height:102px;background:var(--footer);font-size:12px;color:var(--muted)}
.copy{position:absolute;left:74px;top:34px;line-height:19px}
.social{position:absolute;right:74px;top:21px;display:flex;align-items:center;gap:7px;color:#333}
.social-sq{width:25px;height:25px;border-radius:2px}
</style>
</head>
<body>
<div class="page">
  <div class="topbar">Welcome ! <a href="#">Register or Sign In</a></div>

  <nav class="nav">
    <span class="nav-item"><svg viewBox="0 0 14 14"><path d="M2 3h8l2 3v6H2z"/></svg>SELL</span>
    <span class="nav-item"><svg viewBox="0 0 14 14"><circle cx="5" cy="4" r="3"/><path d="M0 13c0-4 10-4 10 0z"/><circle cx="10" cy="4" r="2.5"/></svg>SIGN IN</span>
    <span class="nav-item"><svg viewBox="0 0 14 14"><path d="M0 1h3l2 8h7l2-6H4" fill="none" stroke="#333" stroke-width="1.6"/><circle cx="6" cy="12" r="1.3"/><circle cx="11" cy="12" r="1.3"/></svg>BASKET</span>
    <span class="nav-item"><svg viewBox="0 0 14 14"><path d="M7 0l6 2v5c0 4-3 6-6 7-3-1-6-3-6-7V2z"/></svg>HELP</span>
    <span class="nav-item"><svg viewBox="0 0 14 14"><path d="M1 5c3-4 9-4 12 0v2h-3V5H4v2H1zM3 8h8l1 5H2z"/></svg>CONTACT</span>
  </nav>

  <div class="logo"><span class="logo-mark"></span>Bidwell</div>

  <form class="search">
    <span class="search-label">SEARCH:</span>
    <div class="search-box">
      <span class="search-cat">All Categories</span>
      <span class="search-input"></span>
      <span class="search-gear"></span>
      <span class="search-go"><svg viewBox="0 0 18 18"><circle cx="7" cy="7" r="5" fill="none" stroke="#fff" stroke-width="2"/><path d="M11 11l6 6" stroke="#fff" stroke-width="3"/></svg></span>
    </div>
  </form>

  <div class="rule" style="top:153px"></div>
  <h1 class="section-title">Shop By Categories</h1>
  <div class="rule" style="top:201px"></div>

  <div class="tile" style="left:75px;top:222px;height:198px">
    <div class="ph" role="img" aria-label="Photo of menswear on shop mannequins" style="background:linear-gradient(135deg,#e8e6e2,#b9ad95 60%,#8a8070)"></div>
    <span class="tile-label" style="left:16px;top:148px">Fashion</span>
  </div>
  <div class="tile" style="left:75px;top:435px;height:197px">
    <div class="ph" role="img" aria-label="Photo of a family gardening in a raised bed" style="background:linear-gradient(160deg,#b8b2a8,#7d8a5a 55%,#4a4030)"></div>
    <span class="tile-label" style="left:16px;top:149px">Home &amp; Garden</span>
  </div>
  <div class="tile" style="left:344px;top:222px;height:410px">
    <div class="ph" role="img" aria-label="Photo of a hand using a smartphone in a car mount" style="background:linear-gradient(100deg,#2a3a28,#3f8f2a 45%,#4ad12a 70%,#c9a890)"></div>
    <span class="tile-label" style="left:16px;top:339px">Electricals &amp;<br>Technology</span>
  </div>
  <div class="tile" style="left:614px;top:222px;height:128px">
    <div class="ph" role="img" aria-label="Photo of plush soft toys" style="background:linear-gradient(135deg,#f2d8c8,#d9833a 50%,#cf5a7a)"></div>
    <span class="tile-label" style="left:14px;top:79px">Toys</span>
  </div>
  <div class="tile" style="left:614px;top:364px;height:127px">
    <div class="ph" role="img" aria-label="Photo of a basketball and football" style="background:linear-gradient(135deg,#f4f4f4,#e0e0e0 50%,#c66a2c 75%,#ddd)"></div>
    <span class="tile-label" style="left:14px;top:79px">Sports &amp; Leisure</span>
  </div>
  <div class="tile" style="left:614px;top:505px;height:127px">
    <div class="ph" role="img" aria-label="Photo of a silver SUV on a mountain road" style="background:linear-gradient(180deg,#6a7480,#b0b6bc 50%,#5a4a3c)"></div>
    <span class="tile-label" style="left:0;top:78px">Motors</span>
  </div>
  <div class="tile" style="left:884px;top:222px;height:198px">
    <div class="ph" role="img" aria-label="Photo of an antique pocket watch" style="background:linear-gradient(135deg,#2a1a12,#7a4a2a 50%,#c8905a)"></div>
    <span class="tile-label" style="left:13px;top:126px">Collectables &amp;<br>Antiques</span>
  </div>
  <div class="tile" style="left:884px;top:435px;height:197px">
    <div class="ph" role="img" aria-label="Photo of a model wearing jewellery" style="background:linear-gradient(135deg,#5a5050,#a88878 50%,#e6e0dc)"></div>
    <span class="tile-label" style="left:13px;top:126px">Jewellery &amp;<br>Beauty</span>
  </div>

  <section class="box" style="left:74px">
    <h2>Welcome</h2>
    <p>Even if you're new or already experienced, we have everything you need to enjoy shopping on bidwell.co.uk</p>
    <a class="learn" href="#">LEARN MORE</a>
  </section>

  <section class="box" style="left:344px">
    <h2>Sign In</h2>
    <p>Sign-in to your account in order to buy, sell or manage your preferences.</p>
    <div class="btns"><a class="btn btn-primary" href="#">SIGN IN</a><a class="btn btn-secondary" href="#">REGISTER</a></div>
    <p class="note">Don't have an account? <a href="#">Register ›</a></p>
  </section>

  <section class="box confidence" style="left:614px">
    <h2>Shop with Confidence</h2>
    <div class="feature">
      <svg viewBox="0 0 34 34"><path d="M17 2l12 4v10c0 8-6 13-12 16C11 29 5 24 5 16V6z" fill="#3a9a3a"/><path d="M11 17l4 4 8-9" fill="none" stroke="#fff" stroke-width="3"/></svg>
      <div><strong>Completely safe</strong><span>Bid on or buy items you're watching or searching for</span></div>
    </div>
    <div class="feature">
      <svg viewBox="0 0 34 34"><path d="M9 3h16v8c0 6-4 10-8 10s-8-4-8-10z" fill="#e0a820"/><path d="M9 6H4c0 5 3 7 6 7M25 6h5c0 5-3 7-6 7" fill="none" stroke="#e0a820" stroke-width="2"/><rect x="15" y="21" width="4" height="6" fill="#c89010"/><rect x="10" y="27" width="14" height="4" fill="#c89010"/></svg>
      <div><strong>Premium sellers</strong><span>Great service and the best delivery when you buy from premium sellers.</span></div>
    </div>
    <div class="feature">
      <svg viewBox="0 0 34 34"><rect x="2" y="8" width="30" height="12" rx="2" fill="#2a7ad0"/><g fill="#fff"><circle cx="8" cy="14" r="1.5"/><circle cx="13" cy="14" r="1.5"/><circle cx="18" cy="14" r="1.5"/><circle cx="23" cy="14" r="1.5"/></g><path d="M22 18v10l3-3 3 5" fill="none" stroke="#333" stroke-width="1.5"/></svg>
      <div><strong>Feedback rating system</strong><span>View seller history and feedback of users before you bid or buy.</span></div>
    </div>
  </section>

  <div class="promo" role="img" aria-label="Promotional artwork for The Bright Trade Hour Podcast with a studio microphone"></div>

  <footer class="footer">
    <div class="copy">Copyright ©2014,. <a href="#">Bidwell</a><br><a href="#">Powered by: AuctionCore</a></div>
    <div class="social">Connect Us:
      <span class="social-sq" style="background:#3b5a9a" role="img" aria-label="Social network link"></span>
      <span class="social-sq" style="background:#33aadf" role="img" aria-label="Social network link"></span>
      <span class="social-sq" style="background:#d03e2c" role="img" aria-label="Social network link"></span>
      <span class="social-sq" style="background:#c8151e" role="img" aria-label="Social network link"></span>
    </div>
  </footer>
</div>
</body>
</html>
```